Varlow Landscaping

Create a website for a new landscaping company. I have a logo already and description of services offered. I have a website that I would like all inquiries and appointments to get forwarded to. I need just need it well organized so that a husband and wife team can manage it easily. This is a company that will continue to grow over time and will need to add more services under new tabs over time. If you need the email where appointments and inquiries should go please send me a message.
Services offered are: Weekly/bi weekly mowing, weed eating and edging, Plant installation pinestraw & mulch installation, weed & feed, leaf removal and yard clean up.

```html
<!DOCTYPE html>
<html lang="en">
<head>
<meta charset="UTF-8">
<title>Varlow – Lawn Care & Landscaping</title>
<link href="https://fonts.googleapis.com/css2?family=Inter:wght@400;500;600;700;800&display=swap" rel="stylesheet">
<style>
  :root{
    --green:#3fd77f;
    --green-btn-a:#22c55e;
    --green-btn-b:#16a34a;
    --white:#ffffff;
    --text-soft:rgba(255,255,255,0.88);
    --glass:rgba(255,255,255,0.12);
    --glass-line:rgba(255,255,255,0.28);
    --badge-bg:rgba(34,197,94,0.18);
    --badge-line:rgba(74,222,128,0.45);
    --badge-text:#86efac;
  }
  *{box-sizing:border-box;margin:0;padding:0}
  html,body{width:1200px;height:638px;overflow:hidden}
  body{font-family:"Inter",sans-serif;color:var(--white);position:relative;background:#0f2417}
  .hero-photo{
    position:absolute;inset:0;
    background:
      radial-gradient(ellipse 380px 320px at 1080px 480px, rgba(214,210,40,0.75), transparent 70%),
      radial-gradient(ellipse 420px 300px at 900px 200px, rgba(110,150,40,0.75), transparent 70%),
      radial-gradient(ellipse 360px 260px at 560px 520px, rgba(90,120,30,0.7), transparent 70%),
      linear-gradient(90deg,#1b2a2e 0%,#1f3a22 30%,#2e4d1c 60%,#566d1a 100%);
  }
  .hero-shade{position:absolute;inset:0;background:linear-gradient(90deg,rgba(8,20,12,0.55),rgba(8,20,12,0.25))}
  .nav{position:absolute;top:11px;left:195px;right:195px;height:32px;display:flex;align-items:center;justify-content:space-between}
  .brand{display:flex;align-items:center;gap:6px}
  .brand-mark{width:32px;height:32px;border-radius:7px;background:rgba(255,255,255,0.12);border:1px solid var(--glass-line)}
  .brand-name{font-size:13px;font-weight:700;line-height:1.1}
  .brand-tag{font-size:7.5px;font-weight:500;color:var(--text-soft);margin-top:2px}
  .nav-links{display:flex;align-items:center;gap:21px;font-size:11px;font-weight:500}
  .nav-cta{background:linear-gradient(90deg,var(--green-btn-a),var(--green-btn-b));padding:0 15px;height:32px;line-height:32px;border-radius:16px;font-weight:600;margin-left:0}
  .hero-content{position:absolute;left:344px;top:145px;width:520px}
  .badge{display:inline-block;height:22px;line-height:20px;padding:0 11px;border-radius:11px;background:var(--badge-bg);border:1px solid var(--badge-line);color:var(--badge-text);font-size:9.5px;font-weight:500}
  .headline{margin-top:13px;font-size:46px;font-weight:800;letter-spacing:-1.4px;line-height:48px}
  .headline .accent{display:block;color:var(--green)}
  .lead{margin-top:15px;font-size:12.5px;line-height:21px;color:var(--text-soft);letter-spacing:-0.2px}
  .actions{display:flex;gap:11px;margin-top:26px}
  .btn{height:41px;border-radius:21px;display:flex;align-items:center;gap:7px;font-size:12px;font-weight:600;padding:0 21px}
  .btn-primary{background:linear-gradient(90deg,var(--green-btn-a),var(--green-btn-b))}
  .btn-ghost{background:var(--glass);border:1px solid var(--glass-line)}
  .stats{position:absolute;top:444px;left:322px;width:556px;display:flex;justify-content:space-between}
  .stat{width:200px;text-align:center}
  .stat-value{font-size:23px;font-weight:700;line-height:28px;display:flex;justify-content:center;align-items:center;gap:1px}
  .stat-label{font-size:9.5px;color:var(--text-soft);margin-top:3px}
  .scroll-cue{position:absolute;left:600px;top:600px}
</style>
</head>
<body>
  <div class="hero-photo" role="img" aria-label="Gardener trimming a green hedge with electric shears"></div>
  <div class="hero-shade"></div>

  <header class="nav">
    <div class="brand">
      <div class="brand-mark"></div>
      <div>
        <div class="brand-name">Varlow</div>
        <div class="brand-tag">Lawn Care &amp; Landscaping</div>
      </div>
    </div>
    <nav class="nav-links">
      <span>Home</span><span>Services</span><span>Gallery</span>
      <span class="nav-cta">Get Started</span>
    </nav>
  </header>

  <main class="hero-content">
    <span class="badge">✨ Your Outdoor Oasis Awaits</span>
    <h1 class="headline">Transform Your <span class="accent">Outdoor Space</span></h1>
    <p class="lead">Expert lawn care and landscaping services delivered with passion. We create stunning outdoor environments that you'll love coming home to.</p>
    <div class="actions">
      <span class="btn btn-primary">Get Free Quote
        <svg width="12" height="12" viewBox="0 0 24 24" fill="none" stroke="#fff" stroke-width="2.2" stroke-linecap="round" stroke-linejoin="round"><path d="M4 12h16M14 6l6 6-6 6"/></svg>
      </span>
      <span class="btn btn-ghost">
        <svg width="13" height="13" viewBox="0 0 24 24" fill="none" stroke="#fff" stroke-width="2" stroke-linecap="round" stroke-linejoin="round"><path d="M22 16.9v3a2 2 0 0 1-2.2 2 19.8 19.8 0 0 1-8.6-3.1 19.5 19.5 0 0 1-6-6A19.8 19.8 0 0 1 2.1 4.2 2 2 0 0 1 4.1 2h3a2 2 0 0 1 2 1.7c.1.9.4 1.8.7 2.7a2 2 0 0 1-.5 2.1L8 9.8a16 16 0 0 0 6 6l1.3-1.3a2 2 0 0 1 2.1-.4c.9.3 1.8.6 2.7.7a2 2 0 0 1 1.7 2z"/></svg>
        (555) 010-2417
      </span>
    </div>
  </main>

  <section class="stats">
    <div class="stat"><div class="stat-value">100+</div><div class="stat-label">Happy Clients</div></div>
    <div class="stat"><div class="stat-value">5<svg width="21" height="21" viewBox="0 0 24 24" fill="#fff"><path d="M12 2l3.1 6.3 6.9 1-5 4.9 1.2 6.8L12 17.8 5.8 21l1.2-6.8-5-4.9 6.9-1z"/></svg></div><div class="stat-label">Rating</div></div>
    <div class="stat"><div class="stat-value">10+</div><div class="stat-label">Years Experience</div></div>
  </section>

  <svg class="scroll-cue" width="16" height="16" viewBox="0 0 24 24" fill="none" stroke="#fff" stroke-width="2" stroke-linecap="round" stroke-linejoin="round"><path d="M12 4v16M6 14l6 6 6-6"/></svg>
</body>
</html>
```